ORK Brantell Services - Partnership Proposal

My company ORK is a study abroad consultant and We want to send a proposal to Universities and Educational institutions to partner with us. This proposal shall be used by our marketing team to collaborate with more than 100 top universities of the world and hence it must look like an extremely professional presentation.

Target Market(s)

Education institutions and Universities

Industry/Entity Type

Education

Font styles to use
Serif

Colors

Designer to choose colors to be used in the design.

Requirements
Must have
• A professional and neat look with company logo.
Nice to have
• Would like to see some the text presented in an interesting eye catchy manner.
Should not have
• Should not have too many colours or different fonts

```html
<!DOCTYPE html>
<html lang="en">
<head>
<meta charset="utf-8">
<title>ORK Brantell Services – Partnership Proposal</title>
<link href="https://fonts.googleapis.com/css2?family=Arimo:ital,wght@0,400;0,700;1,700&display=swap" rel="stylesheet">
<style>
  :root {
    --paper: #f1f3f3;
    --teal: #34e6d6;
    --teal-light: #5fe8de;
    --teal-deep: #2cbcae;
    --teal-dark: #1fa89b;
    --ink: #1d1f20;
    --bar-dark: #2b2d2e;
    --bar-mid: #5c5f61;
    --white: #ffffff;
  }
  * { margin: 0; padding: 0; box-sizing: border-box; }
  html, body { width: 1200px; height: 849px; overflow: hidden; background: var(--paper); }
  body { font-family: "Arimo", Arial, sans-serif; color: var(--ink); }

  .brochure { position: relative; width: 1200px; height: 849px; overflow: hidden; }
  .backdrop { position: absolute; inset: 0; }

  .conclusion { position: absolute; left: 49px; top: 54px; width: 520px; }
  .conclusion__title {
    font-style: italic; font-weight: 700; font-size: 27px;
    color: var(--teal); letter-spacing: 0.5px; margin-bottom: 6px;
  }
  .conclusion__text { font-size: 15.5px; line-height: 19px; color: var(--ink); }

  .contact-row { position: absolute; left: 45px; display: flex; align-items: center; }
  .contact-row--web { top: 176px; gap: 17px; }
  .contact-row--social { top: 269px; gap: 17px; }
  .contact-row--channels { top: 362px; gap: 12px; }
  .contact-icon {
    width: 58px; height: 58px; border-radius: 50%;
    background: var(--teal-deep); flex: none;
  }
  .contact-icon--small { width: 56px; height: 56px; margin-right: 3px; }
  .contact-bar {
    height: 61px; display: flex; align-items: center; justify-content: center;
    font-style: italic; font-weight: 700; color: var(--white);
  }
  .contact-bar--wide { width: 412px; background: var(--bar-dark); font-size: 31px; }
  .contact-bar--half { width: 166px; background: var(--bar-mid); font-size: 26px; }

  .brand {
    position: absolute; width: 220px; text-align: center;
    font-weight: 700; font-size: 38px; line-height: 42px; color: var(--ink);
  }
  .brand--top { left: 616px; top: 60px; }
  .brand--bottom { left: 314px; top: 696px; }

  .cover-title {
    position: absolute; left: 760px; top: 645px; width: 400px;
    text-align: center; font-style: italic; font-weight: 700;
    font-size: 38px; line-height: 47px; color: var(--white); letter-spacing: 0.5px;
  }
</style>
</head>
<body>
<main class="brochure">
  <svg class="backdrop" width="1200" height="849" viewBox="0 0 1200 849" aria-hidden="true">
    <defs>
      <linearGradient id="studentPhotoTone" x1="0" y1="0" x2="1" y2="1">
        <stop offset="0" stop-color="#e9eeee"/>
        <stop offset="0.45" stop-color="#c9d3d6"/>
        <stop offset="1" stop-color="#9fb6c4"/>
      </linearGradient>
    </defs>
    <rect x="0" y="0" width="600" height="849" fill="var(--paper)"/>
    <polygon points="0,495 275,655 0,849" fill="var(--teal-light)"/>
    <polygon points="275,655 600,410 600,849 0,849" fill="var(--teal)"/>
    <rect x="600" y="0" width="600" height="849" fill="var(--teal)"/>
  </svg>

  <svg class="backdrop" width="1200" height="849" viewBox="0 0 1200 849"
       role="img" aria-label="Photo of a smiling student at a desk with a classmate">
    <polygon points="600,0 1200,0 1200,395 760,620 600,620" fill="url(#studentPhotoTone)"/>
  </svg>

  <svg class="backdrop" width="1200" height="849" viewBox="0 0 1200 849" aria-hidden="true">
    <polygon points="600,0 1015,0 1080,185 600,300" fill="var(--teal)" opacity="0.92"/>
    <polygon points="600,300 690,280 600,420" fill="var(--teal-light)" opacity="0.6"/>
    <polygon points="760,620 1200,395 1200,849 600,849 600,620" fill="var(--teal)"/>
    <polygon points="700,720 760,630 1200,440 1200,849 820,849" fill="var(--teal-dark)"/>
    <polygon points="760,630 1200,440 1200,520 840,650" fill="var(--teal-deep)" opacity="0.7"/>
  </svg>

  <section class="conclusion">
    <h2 class="conclusion__title">CONCLUSION</h2>
    <p class="conclusion__text">We are confident in our ability to create a mutually successful, meaningful and sustainable partnership with your institution. We look forward to the opportunity.</p>
  </section>

  <div class="contact-row contact-row--web">
    <span class="contact-icon"></span>
    <span class="contact-bar contact-bar--wide">www.orkbrantell.com</span>
  </div>
  <div class="contact-row contact-row--social">
    <span class="contact-icon"></span>
    <span class="contact-bar contact-bar--wide">orkbrantell</span>
  </div>
  <div class="contact-row contact-row--channels">
    <span class="contact-icon"></span>
    <span class="contact-bar contact-bar--half">orkbrantell</span>
    <span class="contact-icon contact-icon--small"></span>
    <span class="contact-bar contact-bar--half">orkbrantell</span>
  </div>

  <div class="brand brand--top">ORK Brantell Services</div>
  <div class="brand brand--bottom">ORK Brantell Services</div>

  <h1 class="cover-title">PROPOSAL TO REPRESENT YOUR INSTITUTION</h1>
</main>
</body>
</html>
```